Industrial Automation company requires a business card design

Valtrin Automation provides design & build of Automated Equipment for manufacturing industry.
www.valtrinautomation.example
The equipment we design is used for manufacturing in sectors such as medical device, pharmaceutical, aerospace and electronics.
We require a new business card design which incorporates our (New) logo and the key message words:
Automated Equipment:
Design, Build, Control, Test, Support

```html
<!DOCTYPE html>
<html lang="en">
<head>
<meta charset="utf-8">
<title>Valtrin Automation – Business Card</title>
<link rel="stylesheet" href="https://fonts.googleapis.com/css2?family=Montserrat:wght@300;700;800&display=swap">
<style>
  :root {
    --bg-top: #45497a;
    --bg-bottom: #7aa0ab;
    --card-white: #ffffff;
    --card-black: #000000;
    --brand-green: #11823b;
    --ink-dark: #111111;
    --card-radius: 26px;
  }
  * { box-sizing: border-box; margin: 0; padding: 0; }
  html, body {
    width: 1200px;
    height: 856px;
    overflow: hidden;
  }
  body {
    background: linear-gradient(170deg, var(--bg-top), var(--bg-bottom));
    font-family: "Montserrat", sans-serif;
    position: relative;
  }
  .card {
    position: absolute;
    width: 540px;
    height: 310px;
    border-radius: var(--card-radius);
    overflow: hidden;
  }
  /* Front: brand name */
  .card--front {
    left: 600px;
    top: 110px;
    background: var(--card-white);
    display: flex;
    align-items: center;
    justify-content: center;
    gap: 18px;
  }
  .brand-dot {
    width: 46px;
    height: 46px;
    border-radius: 50%;
    background: var(--brand-green);
    flex: none;
  }
  .brand-name {
    color: var(--brand-green);
    font-weight: 800;
    font-size: 34px;
    letter-spacing: 0.06em;
    text-transform: uppercase;
    line-height: 1.05;
  }
  .brand-name span { display: block; font-size: 19px; letter-spacing: 0.42em; }
  /* Back: key message */
  .card--back {
    left: 60px;
    top: 440px;
    background: var(--card-black);
  }
  .divider {
    position: absolute;
    left: 0;
    top: 0;
    width: 100%;
    height: 100%;
  }
  .tagline-label {
    position: absolute;
    left: 0;
    width: 100%;
    top: 121px;
    text-align: center;
    font-weight: 700;
    font-size: 21px;
    letter-spacing: 0.01em;
    color: var(--ink-dark);
    text-transform: uppercase;
  }
  .services {
    position: absolute;
    left: 0;
    width: 100%;
    top: 190px;
    text-align: center;
    color: var(--brand-green);
    font-size: 27px;
    white-space: nowrap;
  }
  .services .strong { font-weight: 800; }
  .services .light { font-weight: 300; }
</style>
</head>
<body>

  <section class="card card--front" aria-label="Business card front">
    <span class="brand-dot" aria-hidden="true"></span>
    <h1 class="brand-name">Valtrin<span>Automation</span></h1>
  </section>

  <section class="card card--back" aria-label="Business card back">
    <svg class="divider" viewBox="0 0 540 310" aria-hidden="true">
      <line x1="0" y1="136" x2="540" y2="136" stroke="#11823b" stroke-width="2.5"/>
      <polygon points="112,136 126,114 414,114 428,136 414,158 126,158" fill="#11823b"/>
    </svg>
    <p class="tagline-label">Automated Equipment:</p>
    <p class="services">
      <span class="strong">Design</span>
      <span class="light">Build</span>
      <span class="strong">Control</span>
      <span class="light">Test</span>
      <span class="strong">Support</span>
    </p>
  </section>

</body>
</html>
```